Corporate Identity for Velta - Waste management company
Letterhead, Business Card, Leaflet, Envelopes, Complimentary Card,
Simple
Marek Lisowiak
Office Management
Velta House
Tallent Wharf
Brenlow Estate
East Pelham Road
London
E14 7QN
marek@velta-waste.example
www.velta-waste.example
For our stationery we would like to include (preferably at the bottom of the page) :
Registered Office: 7th Floor Fenmore House, 42 Halden Crest Street, London, EC3R 8TD. Registered in England No: 07392846
and 6 logo certificates.
For business cards:
- please add dd and mobile number as well. We will need business cards for 3-5 different people.
No toll free number anywhere.
Delete other 2 websites and keep only one:
Footer
Please attach 7 logo certificates on letterhead and price lists.
please use just VELTA
Footer pic 1-7
Footer pic 2-7
Footer pic 3-7
Footer pic 4-7
Footer pic 5-7
Footer 6-7
Footer pic 7-7
Price List Landscape
Price List Portrait
Form 1
Form 2
Form 3
Logo certificates for letter head.

```html
<!DOCTYPE html>
<html lang="en">
<head>
<meta charset="utf-8">
<title>Velta business cards</title>
<link rel="stylesheet" href="https://fonts.googleapis.com/css2?family=Arimo:wght@400;700&display=swap">
<style>
:root{
  --navy:#163a5c;
  --navy-deep:#0f2c48;
  --green:#8dc63f;
  --green-dark:#5f9e2f;
  --white:#ffffff;
  --paper:#f3f4f5;
  --stage:#e4e1dc;
  --ink:#3c4650;
}
*{box-sizing:border-box;margin:0;padding:0}
html,body{width:1200px;height:571px;overflow:hidden}
body{background:var(--stage);font-family:"Arimo",Arial,sans-serif;position:relative}
.card{position:absolute;border-radius:8px;overflow:hidden;box-shadow:0 3px 8px rgba(0,0,0,.25)}
.card--front{top:43px;width:312px;height:240px;background:var(--white)}
.card--front-a{left:271px}
.card--front-b{left:605px}
.card__band{position:absolute;left:0;top:0;width:312px;height:110px}
.card__name{position:absolute;right:16px;top:14px;text-align:right;color:var(--white)}
.card__name strong{display:block;font-size:17px;font-weight:700}
.card__name span{display:block;font-size:8px;margin-top:2px}
.brand{position:absolute;display:flex;align-items:center;gap:8px;color:var(--navy)}
.brand__dot{border-radius:50%;background:var(--navy)}
.brand__name{font-weight:700;letter-spacing:1px}
.card--front-a .brand{left:20px;top:118px}
.card--front-a .brand__dot{width:34px;height:34px}
.card--front-a .brand__name{font-size:34px}
.card--front-b .brand{left:18px;top:178px}
.card--front-b .brand__dot{width:34px;height:34px}
.card--front-b .brand__name{font-size:32px}
.contact{position:absolute;font-size:6.5px;line-height:1.45;color:var(--ink);white-space:nowrap}
.card--front-a .contact--address{left:16px;top:186px}
.card--front-a .contact--numbers{left:134px;top:186px}
.card--front-a .contact--web{left:206px;top:186px}
.card--front-b .contact--address{left:188px;top:112px}
.card--back{top:300px;width:276px;height:192px}
.card--back-white{left:156px;background:linear-gradient(135deg,var(--white),#e8e9eb)}
.card--back-navy{left:456px;background:var(--navy)}
.card--back-green{left:756px;background:var(--green)}
.card__mark{position:absolute;left:50%;top:50%;transform:translate(-50%,-56%);display:flex;align-items:center;gap:8px}
.card__mark .brand__dot{width:46px;height:46px}
.card__mark .brand__name{font-size:20px}
.card--back-white .brand__dot{background:var(--navy)}
.card--back-white .card__mark{color:var(--navy)}
.card--back-navy .brand__dot,.card--back-green .brand__dot{background:var(--white)}
.card--back-navy .card__mark,.card--back-green .card__mark{color:var(--white)}
.card__web{position:absolute;left:0;right:0;bottom:12px;text-align:center;font-size:6.5px}
.card--back-white .card__web{color:var(--ink)}
.card--back-navy .card__web,.card--back-green .card__web{color:var(--white)}
</style>
</head>
<body>
<section class="card card--front card--front-a">
  <svg class="card__band" viewBox="0 0 312 110" aria-hidden="true">
    <path d="M0 0H312V70C240 95 150 60 0 90Z" fill="var(--navy)"/>
    <path d="M0 90C150 60 240 95 312 70V80C240 106 150 72 0 100Z" fill="var(--green)"/>
  </svg>
  <div class="card__name"><strong>Marek Lisowiak</strong><span>Office Management</span></div>
  <div class="brand"><span class="brand__dot"></span><span class="brand__name">VELTA</span></div>
  <p class="contact contact--address">Velta House, Tallent Wharf<br>Brenlow Estate, East Pelham Road<br>London, E14 7QN</p>
  <p class="contact contact--numbers">dd 020 7946 0381<br>t 020 7946 0380<br>m 07700 900415</p>
  <p class="contact contact--web">marek@velta-waste.example<br>www.velta-waste.example</p>
</section>

<section class="card card--front card--front-b">
  <svg class="card__band" viewBox="0 0 312 110" aria-hidden="true">
    <path d="M0 0H312V56C220 86 120 44 0 74Z" fill="var(--navy)"/>
    <path d="M0 74C120 44 220 86 312 56V66C220 98 120 56 0 84Z" fill="var(--green)"/>
  </svg>
  <div class="card__name"><strong>Marek Lisowiak</strong><span>Office Management</span></div>
  <p class="contact contact--address">Velta House, Tallent Wharf<br>Brenlow Estate, East Pelham Road<br>London, E14 7QN<br>dd 020 7946 0381<br>t 020 7946 0380<br>m 07700 900415<br>marek@velta-waste.example</p>
  <div class="brand"><span class="brand__dot"></span><span class="brand__name">VELTA</span></div>
</section>

<section class="card card--back card--back-white">
  <div class="card__mark"><span class="brand__dot"></span><span class="brand__name">VELTA</span></div>
  <p class="card__web">www.velta-waste.example</p>
</section>

<section class="card card--back card--back-navy">
  <div class="card__mark"><span class="brand__dot"></span><span class="brand__name">VELTA</span></div>
  <p class="card__web">www.velta-waste.example</p>
</section>

<section class="card card--back card--back-green">
  <div class="card__mark"><span class="brand__dot"></span><span class="brand__name">VELTA</span></div>
  <p class="card__web">www.velta-waste.example</p>
</section>
</body>
</html>
```